Finally a Vodka produced for women ! (Label Design)

We are a small distillery based in Melbourne, Australia and we need a Vodka label design solution that will appeal to women aged 30-50 years and radiate luxury. Full Details are in a design brief attached. We thank you in advance.

Target Market(s)

Affluent females 30-50 years.

Industry/Entity Type

Spirits/Alcohol

Requirements
Must have
• Be clear this is a luxury Vodka.
Nice to have
• Elegance.

```html
<!DOCTYPE html>
<html lang="en">
<head>
<meta charset="utf-8">
<title>Premium Vodka Label – Silver Wren Distillery</title>
<link rel="stylesheet" href="https://fonts.googleapis.com/css2?family=Cinzel+Decorative:wght@400&family=Montserrat:wght@400;600&display=swap">
<style>
  :root {
    --label-plum: #a3368f;
    --blush: #f2b8da;
    --blush-soft: #f6cde5;
    --quartz-rose: #f19cb3;
    --quartz-lilac: #c9a9e0;
    --quartz-mist: #e9dcf0;
  }
  * { margin: 0; padding: 0; box-sizing: border-box; }
  html, body { width: 1200px; height: 1200px; overflow: hidden; }
  body { background: var(--label-plum); font-family: "Montserrat", sans-serif; color: var(--blush); }
  .label { position: relative; width: 1200px; height: 1200px; }
  .label-frame { position: absolute; inset: 0; }
  .crest {
    position: absolute; left: 417px; top: 170px; width: 364px; height: 245px;
    background: radial-gradient(ellipse at 50% 55%, rgba(242,184,218,0.55), rgba(242,184,218,0.15) 70%, transparent 100%);
    border-radius: 40% 40% 50% 50%;
  }
  .product-name {
    position: absolute; left: 0; width: 1200px; top: 418px; text-align: center;
    font-family: "Cinzel Decorative", serif; font-size: 84px; line-height: 1;
    letter-spacing: 2px; color: var(--blush);
  }
  .grade {
    position: absolute; left: 447px; width: 310px; top: 507px; height: 36px;
    display: flex; align-items: center; justify-content: space-between;
    font-size: 26px; font-weight: 600; letter-spacing: 11px; color: var(--blush);
  }
  .grade::before, .grade::after { content: ""; width: 44px; height: 1px; background: var(--blush); }
  .grade span { margin-right: -11px; }
  .filter-badge { position: absolute; left: 496px; top: 574px; width: 200px; height: 200px; }
  .quartz-stone {
    position: absolute; left: 508px; top: 633px; width: 184px; height: 72px;
    background: linear-gradient(100deg, var(--quartz-rose) 0%, var(--quartz-mist) 45%, var(--quartz-lilac) 80%, #8a7fb8 100%);
    clip-path: polygon(4% 40%, 20% 12%, 45% 6%, 70% 4%, 86% 30%, 100% 70%, 72% 100%, 40% 96%, 12% 90%, 0% 70%);
  }
  .origin {
    position: absolute; left: 0; width: 1200px; top: 789px; text-align: center;
    font-size: 17.5px; letter-spacing: 0.5px; color: var(--blush);
  }
  .distillery {
    position: absolute; left: 0; width: 1200px; top: 832px; text-align: center;
    font-weight: 600; color: var(--blush); line-height: 1;
  }
  .distillery-name { display: block; font-size: 40px; letter-spacing: 8px; margin-bottom: 6px; }
  .distillery-type { display: block; font-size: 16px; letter-spacing: 8px; margin-top: 4px; }
  .spec {
    position: absolute; left: 0; width: 1200px; text-align: center;
    font-size: 19px; color: var(--blush);
  }
  .spec-abv { top: 978px; }
  .spec-volume { top: 1012px; font-size: 17px; }
</style>
</head>
<body>
<main class="label">
  <svg class="label-frame" width="1200" height="1200" viewBox="0 0 1200 1200" aria-hidden="true">
    <polygon points="411,145 789,145 1048,794 653,1055 547,1055 152,794" fill="none" stroke="#f2b8da" stroke-width="1.2"/>
  </svg>

  <div class="crest" role="img" aria-label="Ornamental crest of sweeping wings and two swans with filigree scrollwork"></div>

  <h1 class="product-name">VODKA</h1>
  <p class="grade"><span>PREMIUM</span></p>

  <svg class="filter-badge" width="200" height="200" viewBox="0 0 200 200" aria-label="Rose Quartz Filtered">
    <defs>
      <path id="badge-top" d="M 22 100 A 78 78 0 0 1 178 100"/>
      <path id="badge-bottom" d="M 22 100 A 78 78 0 0 0 178 100"/>
    </defs>
    <circle cx="100" cy="100" r="48" fill="#f6cde5" opacity="0.9"/>
    <path d="M 46 70 A 62 62 0 0 1 154 70" fill="none" stroke="#f2b8da" stroke-width="1.2"/>
    <path d="M 46 130 A 62 62 0 0 0 154 130" fill="none" stroke="#f2b8da" stroke-width="1.2"/>
    <text font-family="Montserrat, sans-serif" font-size="15" letter-spacing="2" fill="#f2b8da" text-anchor="middle">
      <textPath href="#badge-top" startOffset="50%">ROSE QUARTZ</textPath>
    </text>
    <text font-family="Montserrat, sans-serif" font-size="15" letter-spacing="2" fill="#f2b8da" text-anchor="middle" dy="12">
      <textPath href="#badge-bottom" startOffset="50%">FILTERED</textPath>
    </text>
  </svg>
  <div class="quartz-stone" role="img" aria-label="Photograph of a raw rose quartz crystal"></div>

  <p class="origin">HANDCRAFTED IN MELBOURNE, AUSTRALIA BY</p>

  <p class="distillery">
    <span class="distillery-name">SILVER</span>
    <span class="distillery-name">WREN</span>
    <span class="distillery-type">DISTILLERY</span>
  </p>

  <p class="spec spec-abv">40% ALC/VOL</p>
  <p class="spec spec-volume">700ml</p>
</main>
</body>
</html>
```